New exciting tequila brand needs fun and attention drawing bottle label.

We need a design for on the glass bottle for a new tequila brand called "Comet Spin Tequila". It can be a label, or the decoration for the entire bottle.
The brand is called "Comet Spin" and is targeting a young party crowd.
I would like the visual to play with the image of a "tiger" & the idea of "up"side down.
In a bar the bottle needs to stand out, so it can be a very colourful design.

Good luck

Target Market(s)

young party crowd

Industry/Entity Type

Crowd

Colors
ec2027
fbed22
f37123
ffffff
f8ba93
fbf289

Requirements
Must have
• tiger
Nice to have
• play with the idea of upside down
Should not have
• have seen it before feeling

```html
<!DOCTYPE html>
<html lang="en">
<head>
<meta charset="utf-8">
<title>Comet Spin Tequila – Bottle Label</title>
<link rel="stylesheet" href="https://fonts.googleapis.com/css2?family=Big+Shoulders+Display:wght@900&display=swap">
<style>
  :root {
    --ink: #231f20;
    --orange: #e6501a;
    --white: #ffffff;
    --page: #ffffff;
  }
  html, body {
    margin: 0;
    padding: 0;
    width: 1200px;
    height: 2286px;
    overflow: hidden;
    background: var(--page);
  }
  .label {
    position: relative;
    width: 1200px;
    height: 2286px;
    background: var(--ink);
    border-radius: 44px;
    overflow: hidden;
    font-family: "Big Shoulders Display", "Arial Narrow", sans-serif;
  }
  .panel {
    position: absolute;
    border-radius: 8px;
  }
  .panel--white { left: 48px; top: 52px; width: 550px; height: 1090px; background: var(--white); }
  .panel--orange { left: 597px; top: 1145px; width: 552px; height: 1092px; background: var(--orange); }

  .tiger-art {
    position: absolute;
    border-radius: 46% 40% 44% 50%;
  }
  .tiger-art--orange { left: 90px; top: 70px; width: 440px; height: 380px;
    background: radial-gradient(ellipse at 45% 45%, var(--orange) 55%, rgba(230,80,26,0.55) 100%); }
  .tiger-art--white-top { left: 660px; top: 765px; width: 450px; height: 365px;
    background: radial-gradient(ellipse at 50% 50%, var(--white) 55%, rgba(255,255,255,0.5) 100%); }
  .tiger-art--white-bottom { left: 110px; top: 1865px; width: 450px; height: 330px;
    background: radial-gradient(ellipse at 50% 50%, var(--white) 55%, rgba(255,255,255,0.5) 100%); }
  .tiger-art--dark { left: 640px; top: 1185px; width: 420px; height: 360px;
    background: radial-gradient(ellipse at 45% 45%, var(--ink) 55%, rgba(35,31,32,0.55) 100%); }

  .lockup {
    position: absolute;
    width: 430px;
    height: 645px;
    overflow: visible;
  }
  .lockup text {
    font-family: "Big Shoulders Display", "Arial Narrow", sans-serif;
    font-weight: 900;
  }
  .lockup--inverted { transform: rotate(180deg); }
  .lockup--tl { left: 125px; top: 465px; fill: var(--ink); }
  .lockup--tl .lockup__spirit { fill: var(--orange); }
  .lockup--tr { left: 645px; top: 100px; fill: var(--white); }
  .lockup--bl { left: 86px; top: 1200px; fill: var(--orange); }
  .lockup--bl .lockup__spirit { fill: var(--white); }
  .lockup--br { left: 668px; top: 1565px; fill: var(--ink); }
</style>
</head>
<body>
<main class="label">
  <div class="panel panel--white"></div>
  <div class="panel panel--orange"></div>

  <div class="tiger-art tiger-art--orange" role="img" aria-label="Orange roaring tiger illustration crouching on the brand name"></div>
  <div class="tiger-art tiger-art--white-top" role="img" aria-label="White tiger illustration hanging upside down below the brand name"></div>
  <div class="tiger-art tiger-art--white-bottom" role="img" aria-label="White tiger illustration hanging upside down below the brand name"></div>
  <div class="tiger-art tiger-art--dark" role="img" aria-label="Black roaring tiger illustration crouching on the brand name"></div>

  <svg class="lockup lockup--tl lockup--inverted" viewBox="0 0 220 330" preserveAspectRatio="none" aria-label="Comet Spin Tequila">
    <text class="lockup__spirit" x="70" y="12" font-size="13" textLength="148" lengthAdjust="spacing">TEQUILA</text>
    <text x="0" y="104" font-size="104" textLength="220" lengthAdjust="spacingAndGlyphs">COMET</text>
    <text x="0" y="328" font-size="265" textLength="220" lengthAdjust="spacingAndGlyphs">SPIN</text>
  </svg>

  <svg class="lockup lockup--tr" viewBox="0 0 220 330" preserveAspectRatio="none" aria-label="Comet Spin Tequila">
    <text class="lockup__spirit" x="70" y="12" font-size="13" textLength="148" lengthAdjust="spacing">TEQUILA</text>
    <text x="0" y="104" font-size="104" textLength="220" lengthAdjust="spacingAndGlyphs">COMET</text>
    <text x="0" y="328" font-size="265" textLength="220" lengthAdjust="spacingAndGlyphs">SPIN</text>
  </svg>

  <svg class="lockup lockup--bl" viewBox="0 0 220 330" preserveAspectRatio="none" aria-label="Comet Spin Tequila">
    <text class="lockup__spirit" x="70" y="12" font-size="13" textLength="148" lengthAdjust="spacing">TEQUILA</text>
    <text x="0" y="104" font-size="104" textLength="220" lengthAdjust="spacingAndGlyphs">COMET</text>
    <text x="0" y="328" font-size="265" textLength="220" lengthAdjust="spacingAndGlyphs">SPIN</text>
  </svg>

  <svg class="lockup lockup--br lockup--inverted" viewBox="0 0 220 330" preserveAspectRatio="none" aria-label="Comet Spin Tequila">
    <text class="lockup__spirit" x="70" y="12" font-size="13" textLength="148" lengthAdjust="spacing">TEQUILA</text>
    <text x="0" y="104" font-size="104" textLength="220" lengthAdjust="spacingAndGlyphs">COMET</text>
    <text x="0" y="328" font-size="265" textLength="220" lengthAdjust="spacingAndGlyphs">SPIN</text>
  </svg>
</main>
</body>
</html>
```